We are a new towing and recovery company starting out in Calhan, CO. We do not want anything generic, we are looking to stand out. we will be doing towing for motorcycles to straight trucks we will have a rollback a 16-ton wrecker and a service vehicle with a wheel lift attached to tow small sized vehicles. We will also be doing roadside services which include lock-out, fuel delivery, jumpstarts, tire changes, and minor auto repair. we will be providing a quality and fast service also customer service will be one of main focuses.

Industry/Entity Type

Wheel

Contact Information for Business Card

Brindle Ridge Towing and Recovery, Dale Hoskin, Owner, 48210 S. Ferrow Road, Pell Springs, CO 80899 555-218-6497 Phone 555-218-6532 Fax www.brindleridgetow.example

```html
<!DOCTYPE html>
<html lang="en">
<head>
<meta charset="utf-8">
<title>Brindle Ridge Towing and Recovery – Business Card</title>
<link rel="stylesheet" href="https://fonts.googleapis.com/css2?family=Open+Sans:ital,wght@0,400;0,600;0,700;1,400&display=swap">
<style>
  :root {
    --page-bg: #d9d9d9;
    --card-bg: #f1f1f0;
    --ink: #111111;
    --accent: #2f3a8f;
    --brand: #2a2d5e;
    --art-top: #e4e4e4;
    --art-bottom: #bdbdbd;
  }
  html, body {
    margin: 0;
    width: 1200px;
    height: 1200px;
    overflow: hidden;
    background: var(--page-bg);
  }
  .canvas {
    width: 1200px;
    height: 1200px;
    display: flex;
    align-items: center;
    justify-content: center;
  }
  .business-card {
    position: relative;
    width: 1050px;
    height: 600px;
    background: var(--card-bg);
    box-shadow: 0 10px 30px rgba(0,0,0,0.18);
    font-family: "Open Sans", sans-serif;
    color: var(--ink);
  }
  .contact {
    position: absolute;
    left: 70px;
    top: 60px;
    width: 470px;
  }
  .contact__name {
    margin: 0 0 0 170px;
    font-size: 44px;
    font-weight: 600;
    line-height: 1.1;
  }
  .contact__title {
    margin: 2px 0 0 260px;
    font-size: 26px;
    font-style: italic;
    color: var(--accent);
  }
  .contact__details {
    margin: 34px 0 0 0;
    text-align: center;
    padding-left: 60px;
  }
  .contact__label {
    display: block;
    font-size: 22px;
    font-style: italic;
    color: var(--accent);
    line-height: 1.1;
    margin-top: 12px;
  }
  .contact__value {
    display: block;
    font-size: 26px;
    font-weight: 700;
    line-height: 1.3;
    letter-spacing: 0.5px;
  }
  .contact__web {
    position: absolute;
    left: 40px;
    bottom: 70px;
    font-size: 26px;
    font-weight: 700;
    letter-spacing: 1.5px;
    color: var(--accent);
  }
  .truck-art {
    position: absolute;
    left: 620px;
    top: 110px;
    width: 380px;
    height: 200px;
    border-radius: 6px;
    background: linear-gradient(180deg, var(--art-top), var(--art-bottom));
  }
  .brand-name {
    position: absolute;
    left: 560px;
    top: 330px;
    width: 480px;
    margin: 0;
    text-align: center;
    font-size: 44px;
    font-weight: 700;
    line-height: 1.15;
    letter-spacing: 4px;
    text-transform: uppercase;
    color: var(--brand);
  }
</style>
</head>
<body>
<main class="canvas">
  <article class="business-card">
    <section class="contact">
      <h1 class="contact__name">Dale Hoskin</h1>
      <p class="contact__title">owner</p>
      <div class="contact__details">
        <span class="contact__label">address:</span>
        <span class="contact__value">48210 S. Ferrow Road,</span>
        <span class="contact__value">Pell Springs, CO 80899</span>
        <span class="contact__label">phone:</span>
        <span class="contact__value">555-218-6497</span>
        <span class="contact__label">fax:</span>
        <span class="contact__value">555-218-6532</span>
      </div>
    </section>
    <div class="contact__web">www.brindleridgetow.example</div>
    <div class="truck-art" role="img" aria-label="Line drawing of a tow truck with a wrecker boom"></div>
    <p class="brand-name">Brindle Ridge<br>Towing<br>and<br>Recovery</p>
  </article>
</main>
</body>
</html>
```